Veltrona 4", 6", 8" DX pumps catalog

A professional clean looking work.

Please put the file named "Write up" for the full description.

For this project, we want the portrait landscape.
Please based the front and back cover design on the two previous jobs, files marked as “Previous Job 1 and Job 2” It will be appreciated if you can come up with two alternatives for the covers: one design on each previous job design
You are free to change the design a little bit so that it is slightly different from the previous job but not too much so that there are still “similarities” and corporate identity.
For the inserts, you are free to deviate from the two previous jobs.
Colors used bright yellow Pantone 803C and dark grey instead of black.
Wordings are all either black or white, not dark grey
Please design the catalog with CYMCK and not with Pantone.

Project Deadline Extended
Reason: Expect the finalization of at least the front and back cover by 11th of November. 11th to 17th is for the finalization of the inserts Dateline required by the 17th and not 22nd as we need the works to be printed on time for the exhibition

Dear Designers, Please submit your front and back cover designs at the earliest

• Clean, professional look, portrait orientation
• Corporate yellow color and dark grey colours used.
• Wordings in black color
• Design in CYMCK and not in pantone
• Some corporate identity with the previous 2 jobs especially for the front and back cover. For the Inserts - you are free to deviate
• Messy

```html
<!DOCTYPE html>
<html lang="en">
<head>
<meta charset="utf-8">
<title>Veltrona Presentation Folder</title>
<link href="https://fonts.googleapis.com/css2?family=Roboto+Condensed:wght@300;400&display=swap" rel="stylesheet">
<style>
  :root {
    --corporate-yellow: #f7dc13;
    --yellow-deep: #e2c41c;
    --yellow-light: #fbe41a;
    --dark-grey: #1e1e1e;
    --dark-grey-soft: #2c2c2c;
    --backdrop: #8a8a8a;
    --white: #ffffff;
    --ink: #111111;
  }
  html, body {
    margin: 0;
    padding: 0;
    width: 1200px;
    height: 907px;
    overflow: hidden;
    background: var(--backdrop);
  }
  .folder {
    display: block;
    width: 1200px;
    height: 907px;
    font-family: "Roboto Condensed", "Arial Narrow", sans-serif;
  }
  .band-url { font-size: 20px; font-weight: 400; }
  .band-url--on-dark { fill: var(--corporate-yellow); }
  .band-url--on-yellow { fill: var(--ink); }
  .contact-text { font-size: 12px; fill: var(--ink); }
  .brand-name { font-size: 30px; font-weight: 400; fill: var(--white); letter-spacing: 2px; }
  .tagline { font-size: 33px; font-weight: 300; fill: var(--corporate-yellow); }
  .contact-icon { fill: var(--ink); }
</style>
</head>
<body>
<svg class="folder" viewBox="0 0 1200 907" xmlns="http://www.w3.org/2000/svg">
  <defs>
    <linearGradient id="back-panel-fill" x1="0" y1="0" x2="1" y2="0">
      <stop offset="0" stop-color="var(--yellow-deep)"/>
      <stop offset="0.6" stop-color="var(--corporate-yellow)"/>
      <stop offset="1" stop-color="var(--yellow-light)"/>
    </linearGradient>
    <linearGradient id="front-panel-fill" x1="0" y1="0" x2="1" y2="0">
      <stop offset="0" stop-color="var(--dark-grey)"/>
      <stop offset="0.7" stop-color="var(--dark-grey-soft)"/>
      <stop offset="1" stop-color="var(--dark-grey)"/>
    </linearGradient>
  </defs>

  <!-- Back panel -->
  <g class="back-panel">
    <path d="M146,55 Q146,43 158,43 H596 V672 L551,845 Q548,857 536,857 H158 Q146,857 146,845 Z" fill="url(#back-panel-fill)"/>
    <rect class="pocket-fold" x="146" y="672" width="450" height="2" fill="#e8cc18" opacity="0.7"/>
    <rect class="url-band" x="146" y="560" width="450" height="28" fill="var(--dark-grey)"/>
    <text class="band-url band-url--on-dark" x="354" y="581" text-anchor="middle">www.veltronapumps.com</text>

    <g class="contact-block">
      <path class="contact-icon" d="M187,604 a4,4 0 0 1 4,4 c0,3 -4,7 -4,7 c0,0 -4,-4 -4,-7 a4,4 0 0 1 4,-4 z M187,606.5 a1.5,1.5 0 1 0 0.01,0 z" fill-rule="evenodd"/>
      <text class="contact-text" x="195" y="613">Veltrona Pumps Pte Ltd</text>
      <text class="contact-text" x="195" y="627">412 Harbourline Road , #05-12C</text>
      <text class="contact-text" x="195" y="641">Kestrel Park Centre, Singapore 604318</text>

      <path class="contact-icon" d="M415,605 l2.5,-1 l2,3.5 l-1.5,1.2 c0.8,1.8 1.8,3 3.2,4 l1.4,-1.3 l3,2.4 l-1.2,2.3 c-5,-0.5 -9.5,-5.5 -9.4,-11.1 z"/>
      <text class="contact-text" x="426" y="613">(65) 6100 2841</text>
      <text class="contact-text" x="426" y="627">(65) 6100 2842</text>
      <rect class="contact-icon" x="414" y="635" width="9" height="6"/>
      <path d="M414,635 l4.5,3.5 l4.5,-3.5" stroke="var(--corporate-yellow)" stroke-width="0.8" fill="none"/>
      <text class="contact-text" x="426" y="641">sales@veltronapumps.com</text>
    </g>
  </g>

  <!-- Front panel -->
  <g class="front-panel">
    <path d="M596,43 H1033 Q1045,43 1045,55 V848 Q1045,860 1033,860 H655 Q643,860 640,848 L596,672 Z" fill="url(#front-panel-fill)"/>
    <rect class="pocket-fold" x="596" y="672" width="449" height="2" fill="#333333"/>

    <g class="brand-lockup">
      <circle cx="820" cy="232" r="26" fill="none" stroke="var(--white)" stroke-width="4"/>
      <text class="brand-name" x="820" y="296" text-anchor="middle">VELTRONA</text>
    </g>
    <rect class="tagline-rule" x="638" y="320" width="366" height="3" fill="var(--corporate-yellow)"/>
    <text class="tagline" x="820" y="369" text-anchor="middle">Made with Pride</text>

    <rect class="url-band" x="596" y="560" width="449" height="28" fill="var(--corporate-yellow)"/>
    <text class="band-url band-url--on-yellow" x="821" y="581" text-anchor="middle">www.veltronapumps.com</text>
  </g>
</svg>
</body>
</html>
```